Designs for a Barrister's chambers

Design stationery (including business card and letterhead) for a barrister's chambers -- similar to a law firm, using the enclosed logo. The current designs are not fit for purpose.

```html
<!DOCTYPE html>
<html lang="en">
<head>
<meta charset="utf-8">
<title>Ledgerline Chambers – Business Card</title>
<link rel="stylesheet" href="https://fonts.googleapis.com/css2?family=Montserrat:wght@700&family=Lato:wght@400;700&display=swap">
<style>
  :root {
    --stage: #2b2c2e;
    --navy: #031a36;
    --navy-emboss: #0a2e5c;
    --ink: #0b1a33;
    --teal: #1a93b0;
    --rule: #b9e0ea;
    --paper: #ffffff;
    --text: #1f2633;
  }
  * { box-sizing: border-box; margin: 0; padding: 0; }
  html, body { width: 1200px; height: 1040px; overflow: hidden; }
  body {
    background: var(--stage);
    font-family: "Lato", sans-serif;
    position: relative;
  }
  .card {
    position: absolute;
    left: 290px;
    width: 620px;
    height: 354px;
  }
  .card--back {
    top: 112px;
    background: var(--navy);
    border-radius: 90px 0 90px 0;
    display: flex;
    align-items: center;
    justify-content: center;
  }
  .card--front {
    top: 548px;
    background: var(--paper);
    border-radius: 0 80px 0 80px;
  }
  .brand {
    display: flex;
    align-items: center;
    gap: 22px;
  }
  .brand__mark {
    width: 84px;
    height: 84px;
    flex: none;
  }
  .brand__name {
    font-family: "Montserrat", sans-serif;
    font-weight: 700;
    font-size: 50px;
    line-height: 0.98;
    letter-spacing: -0.5px;
  }
  .card--back .brand__mark { background: var(--navy-emboss); }
  .card--back .brand__name { color: var(--navy-emboss); }

  .card--front .brand {
    position: absolute;
    top: 52px;
    right: 40px;
  }
  .card--front .brand__mark { background: var(--teal); }
  .card--front .brand__name { color: var(--ink); }

  .holder {
    position: absolute;
    left: 70px;
    top: 178px;
  }
  .holder__name {
    color: var(--teal);
    font-weight: 700;
    font-size: 30px;
    letter-spacing: 0.3px;
  }
  .holder__role {
    color: var(--text);
    font-size: 16px;
    margin-top: -2px;
  }
  .divider {
    position: absolute;
    left: 160px;
    right: 40px;
    top: 233px;
    height: 1px;
    background: var(--rule);
  }
  .contacts {
    position: absolute;
    left: 44px;
    top: 246px;
    list-style: none;
  }
  .contacts li {
    display: flex;
    align-items: center;
    gap: 10px;
    font-size: 17px;
    color: var(--text);
    line-height: 22px;
    letter-spacing: 0.4px;
  }
  .contacts svg { width: 18px; height: 18px; flex: none; }
  .address {
    position: absolute;
    right: 40px;
    bottom: 26px;
    text-align: right;
    font-size: 17px;
    color: var(--text);
    line-height: 24px;
    letter-spacing: 0.4px;
  }
  .address__web { margin-top: 6px; }
  .address__web span { color: var(--teal); }
</style>
</head>
<body>

<section class="card card--back" aria-label="Card back">
  <div class="brand">
    <div class="brand__mark"></div>
    <div class="brand__name">Ledgerline<br>Chambers</div>
  </div>
</section>

<section class="card card--front" aria-label="Card front">
  <div class="brand">
    <div class="brand__mark"></div>
    <div class="brand__name">Ledgerline<br>Chambers</div>
  </div>

  <div class="holder">
    <div class="holder__name">Marcus Hollins</div>
    <div class="holder__role">Barrister</div>
  </div>
  <div class="divider"></div>

  <ul class="contacts">
    <li>
      <svg viewBox="0 0 24 24" fill="none" stroke="#1a93b0" stroke-width="2.2" stroke-linecap="round" stroke-linejoin="round"><path d="M5 3h4l2 5-2.5 1.5a11 11 0 0 0 6 6L16 13l5 2v4a2 2 0 0 1-2 2A16 16 0 0 1 3 5a2 2 0 0 1 2-2z"/></svg>
      0207 946 0123
    </li>
    <li>
      <svg viewBox="0 0 24 24" fill="none" stroke="#1a93b0" stroke-width="2.2" stroke-linejoin="round"><rect x="6" y="2" width="12" height="20" rx="2"/><line x1="11" y1="18" x2="13" y2="18"/></svg>
      07700 900 456
    </li>
    <li>
      <svg viewBox="0 0 24 24" fill="#1a93b0"><rect x="7" y="2" width="10" height="6"/><rect x="2" y="9" width="20" height="9" rx="2"/><rect x="6" y="15" width="12" height="7" fill="#fff" stroke="#1a93b0" stroke-width="2"/></svg>
      0207 946 0124
    </li>
    <li>
      <svg viewBox="0 0 24 24" fill="#1a93b0"><path d="M2 5h20v14H2z"/><path d="M2 5l10 8 10-8" fill="none" stroke="#fff" stroke-width="1.8"/></svg>
      clerks@ledgerlinechambers.com
    </li>
  </ul>

  <div class="address">
    27 Wardrobe Row, London<br>EC4V 9ZX
    <div class="address__web">www.<span>ledgerlinechambers</span>.com</div>
  </div>
</section>

</body>
</html>
```